Ledgerwise Business Card Design

Business Card Design for new business called Ledgerwise focused on selling business software to small and medium size companies who have outgrown Tallymark. Similar companies would be Tallymark, Nuvo, CoreFlow. Also Dealharbor would be good to look at for additional ideas around look and feel.

Target Market(s)

Business to Business

Industry/Entity Type

Information Technology

Contact Information for Business Card

Standard Business Card Information

Font styles to use
Sans Serif

```html
<!DOCTYPE html>
<html lang="en">
<head>
<meta charset="utf-8">
<title>Ledgerwise Business Card</title>
<link href="https://fonts.googleapis.com/css2?family=Open+Sans:wght@400;600;700;800&display=swap" rel="stylesheet">
<style>
  :root {
    --brand-blue: #0b5088;
    --brand-orange: #f5821f;
    --paper: #ffffff;
    --backdrop: #e6e7e9;
    --ink-light: #ffffff;
  }
  * { box-sizing: border-box; margin: 0; padding: 0; }
  html, body { width: 1200px; height: 900px; overflow: hidden; }
  body {
    background: var(--backdrop);
    font-family: "Open Sans", Arial, sans-serif;
    position: relative;
  }
  .card {
    position: absolute;
    width: 640px;
    height: 366px;
    border-radius: 22px;
    overflow: hidden;
    box-shadow: 0 10px 28px rgba(0,0,0,0.18);
  }
  /* Front */
  .card--front { left: 140px; top: 58px; background: var(--paper); }
  .card--front .side-band {
    position: absolute; top: 0; bottom: 0; right: 46px; width: 30px;
    background: var(--brand-blue);
  }
  .wordmark {
    position: absolute;
    display: flex; align-items: center; gap: 14px;
    font-weight: 800; letter-spacing: 0.5px;
  }
  .wordmark .mark-dot {
    width: 46px; height: 46px; border-radius: 50%;
    background: var(--brand-orange); flex: none;
  }
  .card--front .wordmark {
    left: 70px; top: 140px; font-size: 52px; color: var(--brand-blue);
  }
  /* Back */
  .card--back { left: 420px; top: 474px; background: var(--brand-blue); color: var(--ink-light); }
  .card--back .side-band {
    position: absolute; top: 0; bottom: 0; left: 60px; width: 32px;
    background: var(--brand-orange);
  }
  .card--back .wordmark {
    right: 40px; top: 48px; font-size: 44px; color: var(--ink-light);
  }
  .card--back .wordmark .mark-dot { width: 40px; height: 40px; }
  .person {
    position: absolute; right: 40px; top: 146px; text-align: right;
  }
  .person__name { font-size: 24px; font-weight: 700; letter-spacing: 0.3px; }
  .person__title { font-size: 15px; font-weight: 600; color: var(--brand-orange); margin-top: -2px; }
  .rule {
    position: absolute; height: 1px; background: var(--ink-light);
  }
  .rule--name { left: 92px; right: 40px; top: 206px; opacity: 0.9; }
  .rule--contact { left: 92px; width: 300px; top: 268px; opacity: 0.9; }
  .address {
    position: absolute; right: 40px; top: 218px; text-align: right;
    font-size: 14px; font-weight: 600; line-height: 1.4;
  }
  .contact-icons {
    position: absolute; left: 60px; width: 32px; top: 280px;
    display: flex; flex-direction: column; align-items: center; gap: 7px;
  }
  .contact-icons svg { width: 16px; height: 16px; display: block; }
  .contact-list {
    position: absolute; left: 104px; top: 277px;
    list-style: none; font-size: 15px; font-weight: 700; line-height: 23px;
  }
</style>
</head>
<body>

<section class="card card--front" aria-label="Card front">
  <div class="wordmark"><span class="mark-dot"></span><span>Ledgerwise</span></div>
  <div class="side-band"></div>
</section>

<section class="card card--back" aria-label="Card back">
  <div class="side-band"></div>
  <div class="wordmark"><span class="mark-dot"></span><span>Ledgerwise</span></div>

  <div class="person">
    <p class="person__name">Daniel R. Hartley</p>
    <p class="person__title">Director</p>
  </div>
  <div class="rule rule--name"></div>

  <address class="address" style="font-style:normal">
    1420 North Alder Rd<br>| Austin, Texas 78701
  </address>

  <div class="rule rule--contact"></div>

  <div class="contact-icons">
    <svg viewBox="0 0 16 16" aria-hidden="true"><path fill="#fff" d="M4 1.5l2 3-1.3 1.4c.8 1.8 2.2 3.2 4 4L10.1 8.6l3 2-.9 2.6c-5.6 0-10.1-4.5-10.1-10.1z"/></svg>
    <svg viewBox="0 0 16 16" aria-hidden="true"><rect x="1.5" y="3.5" width="13" height="9" fill="none" stroke="#fff" stroke-width="1.4"/><path d="M1.8 4l6.2 5 6.2-5" fill="none" stroke="#fff" stroke-width="1.4"/></svg>
    <svg viewBox="0 0 16 16" aria-hidden="true"><circle cx="8" cy="8" r="6.3" fill="none" stroke="#fff" stroke-width="1.3"/><ellipse cx="8" cy="8" rx="2.6" ry="6.3" fill="none" stroke="#fff" stroke-width="1.1"/><path d="M1.8 8h12.4" stroke="#fff" stroke-width="1.1"/></svg>
  </div>
  <ul class="contact-list">
    <li>(555) 014-2290</li>
    <li>daniel@hartleymail.com</li>
    <li>www.ledgerwise.com</li>
  </ul>
</section>

</body>
</html>
```